Clinique VitaMira business card

I am looking for a talented designer who can an existing design and make it better. I need a 2 sided business card to represent our Psychology clinic staff members. It would need to be elegant, yet modern, clean, light and uplifting. Simple design, quick turnaround time. Lots of files and logos to use as your guide. I hope to hear from you!

Target Market(s)

Clients who receive the card of our therapists

Industry/Entity Type

Health And Wellness

Contact Information for Business Card

Following the similar designs of the Bluepine Care Center card, there will be 2 sides. Side 1 (front) should have the vitamira logo instead of the bluepine care logo, The title should read Clinique VitaMira instead of centre Soins Pinbleu/Bluepine care Center.

Side 2 should have a spiral similar to the one on the card with sunflower leaves, and the title of the Therapist should be Marie Lise Benkirane, Psychologue, Psychologist, her email: Marie@Vitamira-example.com and phone number should be (514) 555-0173

Font styles to use
Serif

Colors
fee18a
85cae6
ffffff
0255a3

Requirements
Must have
• Side 1 (front): vitamira logo- Name of the clinic, clinic address, contact info of clinic etc. use little icons in front of each (just like on sample card)
side 2: Therapist name titles and their contact info underneath with design of spiral and/or sunflower leaves..
Nice to have
• soft colors along soft yellow/gold and blue like the logo,
mini icons for phone, email, address etc.
We do work with a holistic, zen approach so it should represent that to some extent

```html
<!DOCTYPE html>
<html lang="fr">
<head>
<meta charset="utf-8">
<title>Clinique VitaMira – Business Card</title>
<link href="https://fonts.googleapis.com/css2?family=Lato:wght@400;700&display=swap" rel="stylesheet">
<style>
  :root {
    --sun: #fee18a;
    --sun-deep: #f5d33a;
    --sky: #85cae6;
    --white: #ffffff;
    --navy: #0255a3;
    --ink: #1f4f9a;
    --stage: #d9d9d9;
  }
  * { box-sizing: border-box; margin: 0; padding: 0; }
  html, body { width: 1200px; height: 675px; overflow: hidden; }
  body {
    background: var(--stage);
    font-family: "Lato", sans-serif;
    display: flex;
    align-items: center;
    justify-content: center;
    gap: 60px;
  }
  .card {
    width: 520px;
    height: 298px;
    border-radius: 16px;
    position: relative;
    overflow: hidden;
  }
  /* Front */
  .card-front { background: var(--white); color: var(--ink); }
  .brand {
    position: absolute;
    left: 40px; top: 128px;
    display: flex; align-items: center; gap: 10px;
  }
  .brand-dot { width: 26px; height: 26px; border-radius: 50%; background: var(--sun-deep); }
  .brand-name { font-size: 32px; font-weight: 400; color: var(--navy); }
  .divider {
    position: absolute; left: 258px; top: 48px;
    width: 1px; height: 200px; background: var(--sky);
  }
  .clinic {
    position: absolute; left: 282px; top: 52px; right: 20px;
  }
  .clinic-title { font-weight: 700; font-size: 16px; line-height: 1.25; margin-bottom: 12px; }
  .contact { list-style: none; font-size: 13px; line-height: 1.3; }
  .contact li { display: flex; gap: 7px; align-items: flex-start; margin-bottom: 6px; }
  .contact .gap { margin-top: 8px; }
  .contact li.tight { margin-bottom: 1px; }
  .icon { width: 12px; height: 12px; flex: none; margin-top: 2px; fill: var(--sky); }
  /* Back */
  .card-back { background: linear-gradient(160deg, #2466b8, var(--navy)); color: var(--white); }
  .sunflower {
    position: absolute; left: 30px; top: 20px;
    width: 240px; height: 240px; border-radius: 50%;
    background: radial-gradient(circle, var(--sun) 0 35%, var(--sun-deep) 36% 60%, rgba(245,211,58,0) 70%);
  }
  .therapist { position: absolute; right: 40px; bottom: 46px; width: 210px; }
  .therapist-name { font-weight: 700; font-size: 18px; }
  .therapist-role { font-size: 13px; margin: 3px 0 10px; }
  .therapist .contact { font-size: 12px; }
  .therapist .icon { fill: var(--white); }
</style>
</head>
<body>
  <section class="card card-front" aria-label="Card front">
    <div class="brand">
      <span class="brand-dot"></span>
      <span class="brand-name">VitaMira</span>
    </div>
    <div class="divider"></div>
    <div class="clinic">
      <h1 class="clinic-title">Clinique VitaMira<br>Bluepine care Center</h1>
      <ul class="contact">
        <li><svg class="icon" viewBox="0 0 12 12"><path d="M6 0a4 4 0 0 1 4 4c0 3-4 8-4 8S2 7 2 4a4 4 0 0 1 4-4zm0 2.5a1.5 1.5 0 1 0 0 3 1.5 1.5 0 0 0 0-3z"/></svg><span>4810 rue des Érables<br>Pierrefonds, Qc., H9K 2T4</span></li>
        <li><svg class="icon" viewBox="0 0 12 12"><path d="M1 5c0-2 2-3 5-3s5 1 5 3l-2 1-1-1.5H4L3 6zM3 7h6l1 4H2z"/></svg><span>(514) 555-0173</span></li>
        <li class="gap tight"><svg class="icon" viewBox="0 0 12 12"><path d="M0 2h12v8H0zm1 1 5 4 5-4z"/></svg><span>info@vitamira.com</span></li>
        <li class="tight"><svg class="icon" viewBox="0 0 12 12"><circle cx="6" cy="6" r="5.5"/></svg><span>www.vitamira.com</span></li>
        <li class="tight"><svg class="icon" viewBox="0 0 12 12"><rect x="1" y="1" width="10" height="10" rx="2"/></svg><span>www.social-example.net/VitaMira</span></li>
      </ul>
    </div>
  </section>

  <section class="card card-back" aria-label="Card back">
    <div class="sunflower" role="img" aria-label="Yellow sunflower with spiral centre"></div>
    <div class="therapist">
      <h2 class="therapist-name">Marie Lise Benkirane</h2>
      <p class="therapist-role">Psychologue, Psychologist</p>
      <ul class="contact">
        <li class="tight"><svg class="icon" viewBox="0 0 12 12"><rect x="3" y="0.5" width="6" height="11" rx="1"/></svg><span>(514) 555-0173</span></li>
        <li class="tight"><svg class="icon" viewBox="0 0 12 12"><path d="M0 2h12v8H0zm1 1 5 4 5-4z"/></svg><span>Marie@Vitamira-example.com</span></li>
      </ul>
    </div>
  </section>
</body>
</html>
```